Letterhead & Business Card for our Professional Practice (Financial Services)

We are looking for someone to design a letterhead and business card for our business, which is a professional practice called Harbor Lumen Capital Limited. The website is at www.harborrlumencapital.example.co.uk.

The letterhead needs to have: (a) our logo (b) address (c) telephone number (d) email address and (e) our company number.

We would like the stationary to be consistent with the website.

I have attached the logo in EPS and PNG format.

Target Market(s)

Professional services, large commercial enterprises, financial services

Industry/Entity Type

Financial Service

Font styles to use
Serif

Colors
3176b5
f04a50

Requirements
Must have
• Be consistent with our website located at www.harborlumencapital.example.co.uk
• Be in the following formats:
• 1. Word template for the letterhead
• 2. PDF for the letterhead with setup and bleeds required at www.presskite.example.co.uk
• 3. PDF for the business card with setup and bleeds required at www.presskite.example.co.uk
Nice to have
• Something with a really interesting design that says "these guys are professional but dynamic and interesting"
Should not have
• Boring

```html
<!DOCTYPE html>
<html lang="en">
<head>
<meta charset="utf-8">
<title>Harbor Lumen Capital — Stationery</title>
<link rel="stylesheet" href="https://fonts.googleapis.com/css2?family=Alegreya:wght@500&family=Montserrat:wght@500&display=swap">
<style>
  :root {
    --navy: #0d3a73;
    --red: #d2152f;
    --paper: #ffffff;
    --backdrop: #eceae6;
    --blush: #f9e5e7;
    --mist: #e7ebef;
    --brand-font: "Alegreya", Georgia, serif;
    --info-font: "Montserrat", Arial, sans-serif;
  }
  * { box-sizing: border-box; margin: 0; padding: 0; }
  html, body { width: 1200px; height: 800px; overflow: hidden; }
  body { background: var(--backdrop); position: relative; font-family: var(--info-font); color: var(--navy); }

  .sheet { position: absolute; background: var(--paper); box-shadow: 0 4px 14px rgba(0,0,0,.18); overflow: hidden; }

  .brand { display: flex; align-items: center; justify-content: center; gap: 8px; font-family: var(--brand-font); font-weight: 500; color: var(--navy); white-space: nowrap; }
  .brand-square { background: var(--red); flex: none; }

  .rule-band { position: absolute; left: 0; right: 0; border-top: 3px solid var(--red); background: var(--navy); }

  .contacts { display: flex; justify-content: space-between; align-items: flex-start; }
  .contact-line { display: flex; align-items: flex-start; gap: 4px; line-height: 1.3; white-space: nowrap; }
  .contact-line svg { flex: none; fill: none; stroke: var(--navy); }
  .contact-line svg.solid { fill: var(--navy); stroke: none; }

  /* Business card */
  .business-card { left: 101px; top: 228px; width: 385px; height: 232px; }
  .business-card .brand { position: absolute; top: 40px; left: 0; right: 0; font-size: 23px; }
  .business-card .brand-square { width: 16px; height: 16px; }
  .business-card .contacts { position: absolute; top: 155px; left: 24px; right: 20px; font-size: 10px; }
  .business-card .web-phone { padding-top: 2px; }
  .business-card .web-phone .contact-line + .contact-line { margin-top: 6px; }
  .business-card .contact-line svg { width: 9px; height: 9px; margin-top: 2px; }
  .business-card .rule-band { top: 202px; height: 30px; }

  /* Letterhead */
  .letterhead { left: 530px; top: 46px; width: 550px; height: 708px; }
  .letterhead .brand { position: absolute; top: 64px; left: 0; right: 0; font-size: 27px; }
  .letterhead .brand-square { width: 18px; height: 18px; }
  .letterhead .rule-band { top: 103px; height: 19px; }
  .letterhead .backdrop-art { position: absolute; top: 122px; left: 4px; right: 4px; height: 536px;
    background: linear-gradient(180deg, var(--blush) 0%, var(--blush) 62%, var(--mist) 82%, var(--mist) 100%); }
  .letterhead .contacts { position: absolute; left: 24px; right: 22px; top: 662px; font-size: 7.5px; }
  .letterhead .web-phone { padding-top: 6px; }
  .letterhead .contact-line svg { width: 7px; height: 7px; margin-top: 1.5px; }
</style>
</head>
<body>

<section class="sheet business-card" aria-label="Business card">
  <div class="brand"><span class="brand-square"></span>Harbor Lumen Capital</div>
  <div class="contacts">
    <div class="web-phone">
      <div class="contact-line">
        <svg viewBox="0 0 10 10" stroke-width="1"><circle cx="5" cy="5" r="4"/><path d="M1 5h8M5 1c-2 2.5-2 5.5 0 8M5 1c2 2.5 2 5.5 0 8"/></svg>
        www.harborlumencapital.example.co.uk
      </div>
      <div class="contact-line">
        <svg class="solid" viewBox="0 0 10 10"><rect x="1" y="0" width="8" height="10" rx="2"/><rect x="3" y="2" width="4" height="6" fill="#fff"/></svg>
        01632 960418
      </div>
    </div>
    <div class="address contact-line">
      <svg viewBox="0 0 12 10" stroke-width="1"><rect x="0.5" y="1" width="11" height="8"/><path d="M.5 1 6 6l5.5-5"/></svg>
      <div>12-14 Quay Lane<br>Marlow Bucks<br>SL7 4QX</div>
    </div>
  </div>
  <div class="rule-band"></div>
</section>

<section class="sheet letterhead" aria-label="Letterhead">
  <div class="brand"><span class="brand-square"></span>Harbor Lumen Capital</div>
  <div class="rule-band"></div>
  <div class="backdrop-art" role="img" aria-label="Faint large background illustration of a lighthouse beaming light over rolling waves"></div>
  <div class="contacts">
    <div class="web-phone">
      <div class="contact-line">
        <svg viewBox="0 0 10 10" stroke-width="1"><circle cx="5" cy="5" r="4"/><path d="M1 5h8M5 1c-2 2.5-2 5.5 0 8M5 1c2 2.5 2 5.5 0 8"/></svg>
        www.harborlumencapital.example.co.uk
      </div>
      <div class="contact-line">
        <svg class="solid" viewBox="0 0 10 10"><rect x="1" y="0" width="8" height="10" rx="2"/><rect x="3" y="2" width="4" height="6" fill="#fff"/></svg>
        01632 960418
      </div>
    </div>
    <div class="address contact-line">
      <svg viewBox="0 0 12 10" stroke-width="1"><rect x="0.5" y="1" width="11" height="8"/><path d="M.5 1 6 6l5.5-5"/></svg>
      <div>12-14 Quay Lane<br>Marlow Bucks<br>SL7 4QX</div>
    </div>
  </div>
</section>

</body>
</html>
```